Business Card design for amazing new Dental Office

Please read this brief closely!

Our client is a modern new dental office/
They love their new logo.
Now it's time to create a business card for them.

It should be a two sided card:
Side one should have the logo and name and maybe a color background or design.
Side two should have all the contact information which is here:

Marcus Pellow, D.D.S
General and Cosmetic Dentistry
4178 W. Orchard Lane
Ventura, CA 93017
(805) 219-4862
drmarc@bluefernsmiles.example
www.bluefernsmiles.example

Feel free to arrange that info as you like and to style both sides of the card according to your creativity. This is a chance for you to show your design skills!

Client is open to font choices and is looking for a style that is amazing and premium. Colors can be selected from the logo, or any variation of those.

You will not win this contest with a less than beautiful card design so please feel free to make multiple submissions.

Logo files attached and please message me with any questions.
Thanks!

Target Market(s)

Families and Professionals seeking dental services

Industry/Entity Type

Dental

Contact Information for Business Card

Logo, style, contact info as per the brief

Font styles to use
Sans Serif

Requirements
Must have
• Client's logo and contact details as per brief
Nice to have
• Unique style reflecting high end dental clinic near the beach
Should not have
• Must not look like a template

```html
<!DOCTYPE html>
<html lang="en">
<head>
<meta charset="utf-8">
<title>Blue Fern Dental — Business Card</title>
<link rel="stylesheet" href="https://fonts.googleapis.com/css2?family=Arimo:wght@400;700&family=Josefin+Sans:wght@300;400&display=swap">
<style>
  :root {
    --stage: #1f1f1f;
    --sky: #4ab1e2;
    --sky-deep: #3ea6d6;
    --sand: #dca45e;
    --paper: #ffffff;
    --slate: #8a8a8a;
    --teal: #62c2c4;
  }
  * { margin: 0; padding: 0; box-sizing: border-box; }
  html, body { width: 1200px; height: 1059px; overflow: hidden; }
  body { background: var(--stage); position: relative; font-family: "Arimo", Arial, sans-serif; }

  .card {
    position: absolute;
    border-radius: 16px;
    overflow: hidden;
    box-shadow: 0 8px 18px rgba(0,0,0,0.55);
  }

  /* Contact side */
  .card--contact { left: 257px; top: 89px; width: 687px; height: 390px; background: var(--sky); }
  .card__bands { position: absolute; inset: 0; }

  .brand { position: absolute; display: flex; flex-direction: column; align-items: center; text-align: center; }
  .brand__mark { border-radius: 50%; }
  .brand__name, .brand__sub {
    font-family: "Josefin Sans", sans-serif; font-weight: 300; white-space: nowrap;
  }

  .card--contact .brand { left: 76px; top: 32px; width: 200px; }
  .card--contact .brand__mark { width: 54px; height: 54px; background: var(--teal); margin-bottom: 26px; }
  .card--contact .brand__name { font-size: 31px; letter-spacing: 2px; color: var(--slate); line-height: 1; }
  .card--contact .brand__sub { font-size: 13px; letter-spacing: 10px; padding-left: 10px; color: var(--slate); margin-top: 10px; }

  .dentist { position: absolute; right: 360px; top: 258px; text-align: right; white-space: nowrap; }
  .dentist__name { font-weight: 700; font-size: 26px; color: var(--sand); line-height: 1; }
  .dentist__name small { font-size: 19px; }
  .dentist__role { font-size: 16px; color: var(--paper); margin-top: 8px; }
  .divider { position: absolute; left: 348px; top: 252px; width: 1px; height: 66px; background: rgba(255,255,255,0.75); }
  .contact-list { position: absolute; left: 366px; top: 246px; list-style: none; }
  .contact-list li {
    display: flex; align-items: center; gap: 8px;
    font-size: 16.5px; color: var(--paper); height: 27px;
  }
  .contact-list svg { width: 13px; height: 13px; flex: none; }
  .address-band {
    position: absolute; left: 95px; top: 340px; width: 505px; height: 29px;
    background: linear-gradient(90deg, rgba(98,194,196,0) 0%, rgba(98,194,196,0.75) 20%, rgba(98,194,196,0.75) 80%, rgba(98,194,196,0) 100%);
    color: var(--paper); font-size: 16.5px; text-align: center; line-height: 29px;
  }

  /* Brand side */
  .card--brand { left: 253px; top: 546px; width: 694px; height: 395px; background: var(--sky); }
  .card__texture {
    position: absolute; inset: 0;
    background:
      linear-gradient(165deg, rgba(0,0,0,0) 8%, rgba(40,140,195,0.22) 22%, rgba(0,0,0,0) 36%, rgba(40,140,195,0.2) 50%, rgba(0,0,0,0) 64%, rgba(40,140,195,0.2) 78%, rgba(0,0,0,0) 92%);
  }
  .card--brand .brand { left: 0; right: 0; top: 84px; }
  .card--brand .brand__mark { width: 110px; height: 110px; background: rgba(255,255,255,0.92); margin-bottom: 42px; }
  .card--brand .brand__name { font-size: 48px; letter-spacing: 4px; color: var(--paper); line-height: 1; font-weight: 400; }
  .card--brand .brand__sub { font-size: 24px; letter-spacing: 18px; padding-left: 18px; color: var(--paper); margin-top: 16px; font-weight: 400; }
</style>
</head>
<body>

<section class="card card--contact">
  <svg class="card__bands" viewBox="0 0 687 390" preserveAspectRatio="none" aria-hidden="true">
    <path d="M0 0 H687 V65 C560 150 430 205 302 202 C190 199 90 180 0 152 Z" fill="var(--paper)"/>
    <path d="M0 152 C90 180 190 199 302 202 C430 205 560 150 687 65 L687 67 C600 140 470 232 302 231 C190 230 90 215 0 187 Z" fill="var(--sand)"/>
  </svg>

  <div class="brand">
    <span class="brand__mark" aria-hidden="true"></span>
    <div class="brand__name">BLUE FERN</div>
    <div class="brand__sub">DENTAL</div>
  </div>

  <div class="dentist">
    <div class="dentist__name">Marcus Pellow, <small>D.D.S</small></div>
    <div class="dentist__role">General and Cosmetic Dentistry</div>
  </div>

  <div class="divider"></div>

  <ul class="contact-list">
    <li>
      <svg viewBox="0 0 16 16" aria-hidden="true"><path d="M3.5 1.5l2.5 3-1.5 1.8c.8 1.8 2.3 3.3 4.2 4.2L10.5 9l3 2.5-1.6 2.6C6.5 13.5 2.5 9.5 1 4z" fill="var(--sand)"/></svg>
      (805) 219-4862
    </li>
    <li>
      <svg viewBox="0 0 16 16" aria-hidden="true"><rect x="1" y="3" width="14" height="10" fill="var(--sand)"/><path d="M1 3.5l7 5 7-5" stroke="var(--sky)" stroke-width="1.3" fill="none"/></svg>
      drmarc@bluefernsmiles.example
    </li>
    <li>
      <svg viewBox="0 0 16 16" aria-hidden="true"><circle cx="8" cy="8" r="6.5" fill="none" stroke="var(--sand)" stroke-width="1.6"/><path d="M1.5 8h13M8 1.5c-3 3.5-3 9.5 0 13M8 1.5c3 3.5 3 9.5 0 13" stroke="var(--sand)" stroke-width="1.2" fill="none"/></svg>
      www.bluefernsmiles.example
    </li>
  </ul>

  <div class="address-band">4178 W. Orchard Lane Ventura, CA 93017</div>
</section>

<section class="card card--brand">
  <div class="card__texture" role="img" aria-label="Soft diagonal wave pattern in deeper blue tones"></div>
  <div class="brand">
    <span class="brand__mark" aria-hidden="true"></span>
    <div class="brand__name">BLUE FERN</div>
    <div class="brand__sub">DENTAL</div>
  </div>
</section>

</body>
</html>
```